Visitenkarten-Design für Unternehmensberatung
Zielgruppe
Unternehmensberatung, Auswanderungsberatung und Firmengründung in Dubai. Wir suchen ein modernes Design. unserer Zielgruppe sind deutschsprachige Unternehmer
Aufgabenstellung
Lukas Brandeck - CEO
Adresse: Verano Tech Quarter, Building C7, Dubai, VAE
EMail: info@helvor-plan.de
WhatsApp: +49 1609431772
Mobil: +971 506614372
www.helvor-plan.de
(Instagram: https://www.instagram.com/helvor.plan/)

```html
<!DOCTYPE html>
<html lang="de">
<head>
<meta charset="utf-8">
<title>Helvor Plan – Visitenkarte</title>
<link href="https://fonts.googleapis.com/css2?family=Montserrat:wght@400;500;700&family=Crimson+Text:wght@400;700&display=swap" rel="stylesheet">
<style>
  :root {
    --backdrop: #3a3a3c;
    --front-a: #bccbc1;
    --front-b: #a8b1ae;
    --back-a: #e9f1ea;
    --back-b: #d8dbdb;
    --ink: #151716;
    --ink-soft: #3b3f3e;
    --badge: #e4e6e5;
    --icon-fill: #1f3b3e;
    --bar: #565b58;
    --rule: #f4f7f5;
  }
  * { box-sizing: border-box; margin: 0; padding: 0; }
  html, body { width: 1200px; height: 1027px; overflow: hidden; background: var(--backdrop); }
  .canvas { position: relative; width: 1200px; height: 1027px; }

  .card { position: absolute; left: 308px; width: 584px; height: 333px; overflow: hidden; }
  .card--front { top: 126px; background: linear-gradient(200deg, var(--front-a) 0%, var(--front-b) 75%); }
  .card--back { top: 545px; background: linear-gradient(230deg, var(--back-a) 0%, var(--back-b) 100%); }

  .brand-badge { position: absolute; border-radius: 50%; background: var(--badge); }
  .brand-name { position: absolute; font-family: 'Montserrat', sans-serif; font-weight: 700; color: var(--ink); white-space: nowrap; }
  .brand-tagline { position: absolute; font-family: 'Montserrat', sans-serif; font-weight: 400; color: var(--ink-soft); white-space: nowrap; }
  .brand-entity { position: absolute; font-family: 'Montserrat', sans-serif; font-weight: 500; color: var(--ink-soft); white-space: nowrap; }
  .brand-rule { position: absolute; height: 1px; background: linear-gradient(90deg, transparent, var(--rule) 30%, var(--rule) 70%, transparent); }

  .card--front .brand-badge { left: 90px; top: 120px; width: 94px; height: 94px; }
  .card--front .brand-name { left: 198px; top: 124px; font-size: 35px; letter-spacing: 0.5px; }
  .card--front .brand-tagline { left: 200px; top: 168px; font-size: 22.5px; letter-spacing: 0.6px; }
  .card--front .brand-rule { left: 205px; top: 203px; width: 210px; }
  .card--front .brand-entity { left: 413px; top: 199px; font-size: 5.5px; }

  .service-icons { position: absolute; left: 172px; top: 264px; }
  .front-web { position: absolute; left: 0; top: 297px; width: 584px; display: flex; align-items: center; justify-content: center; gap: 10px; }
  .front-web .line { width: 98px; height: 1px; background: linear-gradient(90deg, transparent, var(--ink-soft)); }
  .front-web .line--right { background: linear-gradient(90deg, var(--ink-soft), transparent); }
  .front-web .url { font-family: 'Crimson Text', serif; font-size: 13px; letter-spacing: 3.2px; color: var(--ink); }

  .card--back .brand-badge { left: 37px; top: 36px; width: 43px; height: 43px; }
  .card--back .brand-name { left: 89px; top: 37px; font-size: 17.5px; }
  .card--back .brand-tagline { left: 89px; top: 59px; font-size: 11.5px; letter-spacing: 0.3px; }
  .card--back .brand-rule { left: 89px; top: 76px; width: 100px; background: linear-gradient(90deg, transparent, #c9d5dc, transparent); }
  .card--back .brand-entity { left: 170px; top: 72px; font-size: 3.5px; }

  .person { position: absolute; right: 30px; top: 26px; text-align: right; font-family: 'Crimson Text', serif; color: var(--ink); }
  .person__name { font-size: 23px; font-weight: 700; line-height: 1.05; }
  .person__role { font-size: 18px; line-height: 1.1; }
  .accent-block { position: absolute; left: 557px; top: 25px; width: 27px; height: 55px; background: var(--bar); }

  .contact-list { position: absolute; left: 32px; top: 152px; list-style: none; font-family: 'Crimson Text', serif; color: var(--ink); }
  .contact-list li { display: flex; align-items: center; height: 21.5px; font-size: 17px; }
  .contact-list svg { width: 12px; height: 12px; margin-right: 8px; flex: none; }

  .footer-bar { position: absolute; left: 0; top: 301px; width: 243px; height: 8px; background: var(--bar); }
  .back-web { position: absolute; left: 249px; top: 294px; font-family: 'Crimson Text', serif; font-size: 15.5px; color: var(--ink); }
</style>
</head>
<body>
<main class="canvas">

  <section class="card card--front" aria-label="Vorderseite">
    <div class="brand-badge"></div>
    <div class="brand-name">HELVOR PLAN</div>
    <div class="brand-tagline">CORPORATE SERVICE</div>
    <div class="brand-rule"></div>
    <div class="brand-entity">MERIDANE FZCO</div>

    <svg class="service-icons" width="240" height="24" viewBox="0 0 240 24" aria-label="Leistungen">
      <g fill="var(--icon-fill)">
        <circle cx="11.5" cy="12" r="11"/><circle cx="57.7" cy="12" r="11"/>
        <circle cx="103.9" cy="12" r="11"/><circle cx="150.1" cy="12" r="11"/>
        <circle cx="196.3" cy="12" r="11"/><circle cx="228" cy="12" r="0"/>
      </g>
      <circle cx="242.5" cy="12" r="11" fill="var(--icon-fill)" transform="translate(-0 0)"/>
      <g stroke="#e8eeec" stroke-width="1.2" fill="none" stroke-linecap="round" stroke-linejoin="round">
        <path d="M8 15l7-7M15 8l-1 5M15 8l-5 1"/>
        <rect x="54.7" y="6.5" width="6" height="11" rx="1"/>
        <path d="M99.5 12.5l4.5-4.5h4v4l-4.5 4.5z"/>
        <path d="M146.6 12l2.5 2.5 4.5-5"/>
        <path d="M192.3 17V10h3v7M195.3 17V7h4v10M191.5 17h9"/>
      </g>
    </svg>
    <svg width="24" height="24" viewBox="0 0 24 24" style="position:absolute;left:403px;top:264px" aria-hidden="true">
      <circle cx="12" cy="12" r="11" fill="var(--icon-fill)"/>
      <path d="M6 12h12M12 7l2 5-2 5M9 10l1 2-1 2" stroke="#e8eeec" stroke-width="1.3" fill="none" stroke-linecap="round"/>
    </svg>

    <div class="front-web">
      <span class="line"></span>
      <span class="url">www.helvor-plan.de</span>
      <span class="line line--right"></span>
    </div>
  </section>

  <section class="card card--back" aria-label="Rückseite">
    <div class="brand-badge"></div>
    <div class="brand-name">HELVOR PLAN</div>
    <div class="brand-tagline">CORPORATE SERVICE</div>
    <div class="brand-rule"></div>
    <div class="brand-entity">MERIDANE FZCO</div>

    <div class="person">
      <div class="person__name">Lukas Brandeck</div>
      <div class="person__role">CEO</div>
    </div>
    <div class="accent-block"></div>

    <ul class="contact-list">
      <li>
        <svg viewBox="0 0 12 12"><path d="M6 11.5S2 7 2 4.5a4 4 0 0 1 8 0C10 7 6 11.5 6 11.5z" fill="var(--ink)"/><circle cx="6" cy="4.5" r="1.5" fill="#e3e8e4"/></svg>
        Verano Tech Quarter, Building C7, Dubai, VAE
      </li>
      <li>
        <svg viewBox="0 0 12 12"><rect x="1" y="3" width="10" height="6.5" fill="none" stroke="var(--ink)" stroke-width="0.9"/><path d="M1 3l5 4 5-4" fill="none" stroke="var(--ink)" stroke-width="0.9"/></svg>
        info@helvor-plan.de
      </li>
      <li>
        <svg viewBox="0 0 12 12"><circle cx="6" cy="6" r="5" fill="var(--ink)"/></svg>
        +49 1609431772
      </li>
      <li>
        <svg viewBox="0 0 12 12"><path d="M2.5 1.5l2 .3.8 2.4-1.2 1a6 6 0 0 0 2.7 2.7l1-1.2 2.4.8.3 2c-4.5.8-8.8-3.5-8-8z" fill="var(--ink)"/></svg>
        +971 506614372
      </li>
      <li>
        <svg viewBox="0 0 12 12"><rect x="1.5" y="1.5" width="9" height="9" rx="2" fill="none" stroke="var(--ink)" stroke-width="1"/></svg>
        helvor.plan
      </li>
    </ul>

    <div class="footer-bar"></div>
    <div class="back-web">www.helvor-plan.de</div>
  </section>

</main>
</body>
</html>
```